Lanternleaf - Fresh Asian Cuisine Menu

We need to redo our menu to include pictures of food items. Our restaurant is vibrant, trendy, upscale Chinese cuisine

Requirements
Must have
• Must fit on 8.5x11 paper. We can remove the About Us section if needed but menu cannot be more than 6 pages total. Must include pictures of menu items

```html
<!DOCTYPE html>
<html lang="en">
<head>
<meta charset="utf-8">
<title>Lanternleaf - Fresh Asian Cuisine · Appetizers</title>
<link href="https://fonts.googleapis.com/css2?family=Oswald:wght@500&family=Montserrat:wght@400;700;800&family=Roboto+Condensed:wght@400;700&display=swap" rel="stylesheet">
<style>
  :root {
    --paper: #f7b229;
    --red: #d4262c;
    --red-dark: #b51d22;
    --ink: #2b1a0c;
    --photo-green: #5d7a3a;
    --photo-warm: #c9672e;
    --photo-cream: #d9c7a2;
  }
  * { box-sizing: border-box; margin: 0; padding: 0; }
  html, body { width: 927px; height: 1200px; overflow: hidden; background: var(--paper); }
  .menu-page {
    position: relative; width: 927px; height: 1200px;
    background: var(--paper); color: var(--ink);
    font-family: "Roboto Condensed", sans-serif;
  }
  .frame-outer { position: absolute; inset: 8px; border: 6px solid var(--red); }
  .frame-inner { position: absolute; inset: 26px; border: 2px solid var(--red); }
  .corner-ornament { position: absolute; width: 86px; height: 86px; background: var(--red); opacity: .85; }
  .corner-ornament.tl { top: 30px; left: 30px; clip-path: polygon(0 0,100% 0,100% 12%,12% 12%,12% 100%,0 100%); }
  .corner-ornament.tr { top: 30px; right: 30px; clip-path: polygon(0 0,100% 0,100% 100%,88% 100%,88% 12%,0 12%); }
  .corner-ornament.bl { bottom: 30px; left: 30px; clip-path: polygon(0 0,12% 0,12% 88%,100% 88%,100% 100%,0 100%); }
  .corner-ornament.br { bottom: 30px; right: 30px; clip-path: polygon(88% 0,100% 0,100% 100%,0 100%,0 88%,88% 88%); }

  .menu-header { position: absolute; top: 52px; left: 0; width: 100%; height: 88px; }
  .medallion { position: absolute; top: 6px; width: 78px; height: 78px; border-radius: 50%; background: var(--red); }
  .medallion.left { left: 220px; }
  .medallion.right { left: 628px; }
  .menu-title {
    position: absolute; left: 0; right: 0; top: 10px; text-align: center;
    font-family: "Oswald", sans-serif; font-weight: 500; font-size: 56px; letter-spacing: 1px;
    color: var(--red);
  }
  .header-band { position: absolute; top: 166px; left: 68px; width: 791px; height: 18px; background: var(--red); opacity: .9; }

  .column-divider { position: absolute; left: 462px; top: 218px; width: 3px; height: 842px; background: var(--red); }

  .menu-column { position: absolute; top: 216px; display: flex; flex-direction: column; }
  .menu-column.left { left: 68px; width: 377px; }
  .menu-column.right { left: 482px; width: 377px; }

  .dish { height: 106px; display: flex; gap: 14px; }
  .menu-column.right .dish { flex-direction: row-reverse; }
  .dish-text { flex: 1; padding-top: 4px; }
  .dish-head { display: flex; justify-content: space-between; align-items: flex-start; gap: 6px; }
  .dish-name {
    font-family: "Montserrat", sans-serif; font-weight: 700; font-size: 16.5px; line-height: 1.15;
    color: var(--ink); position: relative; padding-bottom: 6px;
  }
  .dish-name::after { content: ""; position: absolute; left: 0; bottom: 0; width: 44px; height: 2px; background: var(--red); }
  .dish-price { font-family: "Montserrat", sans-serif; font-size: 20px; color: var(--ink); white-space: nowrap; }
  .dish-desc { margin-top: 7px; font-size: 11.5px; line-height: 1.35; max-width: 228px; }
  .dish-desc strong { display: block; font-weight: 700; }
  .spice { display: inline-flex; gap: 3px; vertical-align: middle; margin-left: 8px; }

  .dish-photo {
    width: 88px; height: 88px; flex: none; border: 4px solid var(--red); border-radius: 8px;
    background: linear-gradient(135deg, var(--photo-warm), var(--photo-cream));
  }
  .dish-photo.greens { background: linear-gradient(135deg, var(--photo-green), #9bb26a); }
  .dish-photo.dark { background: linear-gradient(135deg, #3e2a1c, #8a5a36); }
  .dish-photo.red { background: linear-gradient(135deg, #b83a20, #e08a3a); }

  .brand-mark {
    position: absolute; left: 0; right: 0; top: 1078px; display: flex; justify-content: center; align-items: center; gap: 12px;
  }
  .brand-dot { width: 30px; height: 30px; border-radius: 50%; background: var(--red); }
  .brand-name { font-family: "Montserrat", sans-serif; font-weight: 800; font-size: 40px; color: var(--ink); letter-spacing: 1px; }
</style>
</head>
<body>
<main class="menu-page">
  <div class="frame-outer"></div>
  <div class="frame-inner"></div>
  <div class="corner-ornament tl" role="img" aria-label="Chinese fretwork corner ornament"></div>
  <div class="corner-ornament tr" role="img" aria-label="Chinese fretwork corner ornament"></div>
  <div class="corner-ornament bl" role="img" aria-label="Chinese fretwork corner ornament"></div>
  <div class="corner-ornament br" role="img" aria-label="Chinese fretwork corner ornament"></div>

  <header class="menu-header">
    <div class="medallion left" role="img" aria-label="Round Chinese medallion ornament"></div>
    <h1 class="menu-title">APPETIZERS</h1>
    <div class="medallion right" role="img" aria-label="Round Chinese medallion ornament"></div>
  </header>
  <div class="header-band" role="img" aria-label="Chinese key pattern border band"></div>
  <div class="column-divider"></div>

  <section class="menu-column left">
    <article class="dish">
      <div class="dish-text"><div class="dish-head"><h2 class="dish-name">Edamame</h2><span class="dish-price">$4</span></div>
        <p class="dish-desc">Seasoned &amp; boiled soy bean</p></div>
      <div class="dish-photo greens" role="img" aria-label="Photo of seasoned edamame"></div>
    </article>
    <article class="dish">
      <div class="dish-text"><div class="dish-head"><h2 class="dish-name">Scallion Pancakes</h2><span class="dish-price">$6</span></div>
        <p class="dish-desc">Traditional Chinese flatbread folded with oil and minced scallions and pan fried</p></div>
      <div class="dish-photo" role="img" aria-label="Photo of scallion pancakes"></div>
    </article>
    <article class="dish">
      <div class="dish-text"><div class="dish-head"><h2 class="dish-name">Lanternleaf Lettuce Wraps</h2><span class="dish-price">$8</span></div>
        <p class="dish-desc">Seasoned ground chicken drizzled with our top secret homemade sauce served with lettuce wraps</p></div>
      <div class="dish-photo greens" role="img" aria-label="Photo of chicken lettuce wraps"></div>
    </article>
    <article class="dish">
      <div class="dish-text"><div class="dish-head"><h2 class="dish-name">Salt &amp; Pepper Calamari</h2><span class="dish-price">$9</span></div>
        <p class="dish-desc">Crispy Calamari with Green &amp; red peppers and onions</p></div>
      <div class="dish-photo" role="img" aria-label="Photo of salt and pepper calamari"></div>
    </article>
    <article class="dish">
      <div class="dish-text"><div class="dish-head"><h2 class="dish-name">Buddha Bang Shrimp</h2><span class="dish-price">$9</span></div>
        <p class="dish-desc">Crispy fried shrimp tossed in our creamy spicy sauce</p></div>
      <div class="dish-photo red" role="img" aria-label="Photo of crispy shrimp in spicy sauce"></div>
    </article>
    <article class="dish">
      <div class="dish-text"><div class="dish-head"><h2 class="dish-name">Drunken Chicken<span class="spice" role="img" aria-label="spicy"><svg width="22" height="10" viewBox="0 0 22 10"><ellipse cx="11" cy="5" rx="10" ry="3.5" fill="#d4262c"/></svg></span></h2><span class="dish-price">$8</span></div>
        <p class="dish-desc">Chicken, Thai chili in a house made spicy sauce</p></div>
      <div class="dish-photo red" role="img" aria-label="Photo of drunken chicken"></div>
    </article>
    <article class="dish">
      <div class="dish-text"><div class="dish-head"><h2 class="dish-name">Sichuan Spiced Beef<span class="spice" role="img" aria-label="extra spicy"><svg width="46" height="10" viewBox="0 0 46 10"><ellipse cx="11" cy="5" rx="10" ry="3.5" fill="#d4262c"/><ellipse cx="35" cy="5" rx="10" ry="3.5" fill="#d4262c"/></svg></span></h2><span class="dish-price">$9</span></div>
        <p class="dish-desc">Beef Shank, beef tripe, cilantro, peanuts and celery</p></div>
      <div class="dish-photo red" role="img" aria-label="Photo of Sichuan spiced beef"></div>
    </article>
    <article class="dish">
      <div class="dish-text"><div class="dish-head"><h2 class="dish-name">Beef Crispy Bottom Bao</h2><span class="dish-price">$10</span></div>
        <p class="dish-desc">Pan fried crispy bottom Bao, stuffed with beef, drizzled with scallion and sesame (Fresh made to order, takes at least 20 mins to serve)<strong>add Shrimp $1</strong></p></div>
      <div class="dish-photo" role="img" aria-label="Photo of crispy bottom bao buns"></div>
    </article>
  </section>

  <section class="menu-column right">
    <article class="dish">
      <div class="dish-text"><div class="dish-head"><h2 class="dish-name">Crispy Mala Beef<span class="spice" role="img" aria-label="extra spicy"><svg width="46" height="10" viewBox="0 0 46 10"><ellipse cx="11" cy="5" rx="10" ry="3.5" fill="#d4262c"/><ellipse cx="35" cy="5" rx="10" ry="3.5" fill="#d4262c"/></svg></span><br>Jerky</h2><span class="dish-price">$9</span></div>
        <p class="dish-desc">Dry fried shredded beef with various peppers in sesame and peppercorn oil</p></div>
      <div class="dish-photo dark" role="img" aria-label="Photo of crispy mala beef jerky"></div>
    </article>
    <article class="dish">
      <div class="dish-text"><div class="dish-head"><h2 class="dish-name">Fried Chicken<br>Dumplings (6)</h2><span class="dish-price">$6</span></div>
        <p class="dish-desc">Chinese dumpling stuffed with Chicken, Shiitake mushrooms and bamboo shoots</p></div>
      <div class="dish-photo" role="img" aria-label="Photo of fried chicken dumplings"></div>
    </article>
    <article class="dish">
      <div class="dish-text"><div class="dish-head"><h2 class="dish-name">Red Oil Dumplings (6)<span class="spice" role="img" aria-label="spicy"><svg width="22" height="10" viewBox="0 0 22 10"><ellipse cx="11" cy="5" rx="10" ry="3.5" fill="#d4262c"/></svg></span></h2><span class="dish-price">$7</span></div>
        <p class="dish-desc">Chicken filled dumplings in Sichuan red oil sauce drizzled with sesame</p></div>
      <div class="dish-photo red" role="img" aria-label="Photo of red oil dumplings"></div>
    </article>
    <article class="dish">
      <div class="dish-text"><div class="dish-head"><h2 class="dish-name">Pork Egg Rolls (2)</h2><span class="dish-price">$4</span></div>
        <p class="dish-desc">Hand rolled with julienned veggies with our sweet n' sour mustard sauce</p></div>
      <div class="dish-photo" role="img" aria-label="Photo of pork egg rolls"></div>
    </article>
    <article class="dish">
      <div class="dish-text"><div class="dish-head"><h2 class="dish-name">Vegetarian<br>Spring Rolls (3)</h2><span class="dish-price">$4</span></div>
        <p class="dish-desc">Traditional Asian Roll served with a sweet chili sauce</p></div>
      <div class="dish-photo" role="img" aria-label="Photo of vegetarian spring rolls"></div>
    </article>
    <article class="dish">
      <div class="dish-text"><div class="dish-head"><h2 class="dish-name">Garlic Cucumber Salad</h2><span class="dish-price">$7</span></div>
        <p class="dish-desc">Sliced cucumber with a garlic vinaigrette</p></div>
      <div class="dish-photo greens" role="img" aria-label="Photo of garlic cucumber salad"></div>
    </article>
    <article class="dish">
      <div class="dish-text"><div class="dish-head"><h2 class="dish-name">Hot n' Sour Soup<span class="spice" role="img" aria-label="spicy"><svg width="22" height="10" viewBox="0 0 22 10"><ellipse cx="11" cy="5" rx="10" ry="3.5" fill="#d4262c"/></svg></span></h2><span class="dish-price">$4</span></div>
        <p class="dish-desc">Tangy broth with Bamboo shoot, wood ear mushrooms, tofu, egg and carrots</p></div>
      <div class="dish-photo red" role="img" aria-label="Photo of hot and sour soup"></div>
    </article>
    <article class="dish">
      <div class="dish-text"><div class="dish-head"><h2 class="dish-name">West Lake Soup</h2><span class="dish-price">$4</span></div>
        <p class="dish-desc">Light creamy soup with ground beef, diced Shiitake mushroom, tofu, bamboo shoots, egg white and cilantro</p></div>
      <div class="dish-photo dark" role="img" aria-label="Photo of West Lake soup"></div>
    </article>
  </section>

  <footer class="brand-mark">
    <span class="brand-dot"></span>
    <span class="brand-name">LANTERNLEAF</span>
  </footer>
</main>
</body>
</html>
```